Brand new website for global research and investment startup

We need a simple website, maybe 3 pages: landing page with business description, investment philosophy, team and contact info.
We have a logo already that can be incorporated. Please use the logo only, not the text
We like the color green, something along the lines of #3D6C32 as the main color.
We'd like to design the website with geometric shapes in gradations of the base color. The shapes should suggest "work in progress", "built to last (a long time)", "solidity" and "indestructibility". One idea floating in my head sees smaller features with icosahedron and dodecahedron shapes, and maybe larger structures like crystal lattices; but please feel free to be creative and imagine your own.

```html
<!DOCTYPE html>
<html lang="en">
<head>
<meta charset="utf-8">
<title>Keystone Research &amp; Investment</title>
<link rel="stylesheet" href="https://fonts.googleapis.com/css2?family=Space+Grotesk:wght@500;600;700&family=Inter:wght@400;500;600&family=Space+Mono:wght@400;700&display=swap">
<style>
:root{
  --green-dark:#2b5e34;
  --green:#4aa63f;
  --green-text:#3d6c32;
  --green-base:#3d6c32;
  --green-light:#8fbf7f;
  --ink:#15231a;
  --muted:#5d665f;
  --paper:#f9faf5;
  --white:#ffffff;
  --mint:#eef3ea;
  --line:#15231a;
}
*{box-sizing:border-box;margin:0;padding:0}
html,body{width:1200px;height:2825px;overflow:hidden}
body{font-family:"Inter",sans-serif;color:var(--ink);background:var(--paper);font-size:14px}
.wrap{width:760px;margin:0 auto;position:relative;height:100%}
.label{font-family:"Space Mono",monospace;font-size:8.5px;letter-spacing:1.6px;color:var(--green-text);text-transform:uppercase;font-weight:700}
h1,h2,h3,h4{font-family:"Space Grotesk",sans-serif;color:var(--ink)}
.link{font-family:"Space Grotesk",sans-serif;font-weight:700;font-size:10px;letter-spacing:.6px;text-transform:uppercase;color:var(--ink);text-decoration:none;border-bottom:2px solid var(--green);padding-bottom:3px;white-space:nowrap}
.btn{display:inline-block;font-family:"Space Grotesk",sans-serif;font-weight:700;font-size:10px;letter-spacing:.6px;text-transform:uppercase;text-decoration:none;color:var(--ink);background:var(--green);padding:9px 15px;box-shadow:3px 3px 0 var(--line);border:1px solid var(--line);white-space:nowrap}
.btn.ghost{background:var(--white)}
.card{background:var(--white);border:1.5px solid var(--line);box-shadow:4px 4px 0 var(--line);position:absolute}
section{position:relative;border-bottom:1.5px solid var(--line);overflow:hidden}
.geo{position:absolute;pointer-events:none}

/* nav */
.nav{height:50px;background:var(--paper)}
.brand{position:absolute;top:14px;display:flex;align-items:center;gap:8px;font-family:"Space Grotesk",sans-serif;font-weight:700;font-size:13px;color:var(--ink);letter-spacing:.5px}
.brand-mark{width:14px;height:14px;background:var(--green-dark)}
.menu{position:absolute;left:205px;top:19px;display:flex;gap:28px;font-family:"Space Grotesk",sans-serif;font-size:10px;letter-spacing:.8px;font-weight:500}
.nav .btn{position:absolute;right:0;top:11px}

/* hero */
.hero{height:395px}
.hero .label{position:absolute;top:65px}
.hero h1{position:absolute;top:90px;font-size:37px;line-height:40px;font-weight:700;letter-spacing:-.5px}
.hero h1 span{color:var(--green-text)}
.hero p{position:absolute;top:181px;width:360px;font-size:11.5px;line-height:20px;color:var(--muted)}
.hero .btn{position:absolute;top:305px;width:167px;text-align:center;padding:9px 0}
.hero .link{position:absolute;left:180px;top:313px}
.stats{position:absolute;left:461px;top:62px;width:299px;height:232px;background:var(--green-dark);border:1.5px solid var(--line);padding:0 21px;z-index:1}
.stat{height:62px;display:flex;align-items:center;justify-content:space-between;border-bottom:1px solid rgba(255,255,255,.25)}
.stat:first-child{height:88px}
.stat:last-child{border:0;height:80px}
.stat b{font-family:"Space Mono",monospace;font-weight:400;font-size:19px;color:var(--green)}
.stat i{font-style:normal;font-family:"Space Grotesk",sans-serif;font-weight:700;font-size:8px;letter-spacing:.8px;line-height:11px;color:#cfe0c8;text-align:right;width:90px;text-transform:uppercase}

/* about */
.about{height:417px;background:var(--white)}
.about .label{position:absolute;top:65px}
.about h2{position:absolute;top:84px;font-size:28px;line-height:29px;width:230px}
.about > .wrap > p{position:absolute;top:184px;width:236px;font-size:10.1px;line-height:17.5px;color:var(--muted)}
.about .link{position:absolute;top:342px}
.feature{width:242px;height:141px;padding:16px}
.feature .num{position:absolute;right:10px;top:10px;font-family:"Space Mono",monospace;font-size:7.5px;color:#a8b0a9}
.icon{width:29px;height:29px;border:1px solid var(--line);display:flex;align-items:center;justify-content:center}
.feature h4{font-size:11.5px;margin:20px 0 10px}
.feature p,.pcard p,.post p{font-size:9.5px;line-height:15px;color:var(--muted)}

/* philosophy */
.philosophy{height:514px;background:var(--mint)}
.philosophy .label{position:absolute;top:69px}
.philosophy h2{position:absolute;top:85px;font-size:27px;line-height:29px;width:450px;font-weight:600}
.philosophy > .wrap > p{position:absolute;top:153px;width:420px;font-size:10.5px;line-height:17.5px;color:var(--muted)}
.pcard{top:231px;width:243px;height:169px;padding:18px}
.tag{display:inline-block;background:var(--green);border:1px solid var(--line);font-family:"Space Mono",monospace;font-size:8px;padding:4px 5px;color:var(--ink)}
.pcard h4{font-size:12.5px;margin:17px 0 11px}
.philosophy .btn{position:absolute;top:410px}

/* insights */
.insights{height:402px;background:var(--white)}
.insights .label{position:absolute;top:69px}
.insights h2{position:absolute;top:85px;font-size:28px;font-weight:600}
.insights .all{position:absolute;right:0;top:103px}
.post{top:138px;width:243px;height:205px;padding:16px}
.post .meta{font-family:"Space Mono",monospace;font-size:7.5px;letter-spacing:.8px;color:var(--green-text);font-weight:700;margin:14px 0 6px;text-transform:uppercase}
.post h4{font-size:11.5px;line-height:15.5px;margin-bottom:8px}
.post .link{position:absolute;left:16px;right:16px;bottom:17px;font-size:9px}

/* team */
.team{height:753px;background:var(--mint);border-bottom:0}
.team .label{position:absolute;top:69px}
.team h2{position:absolute;top:86px;font-size:28px;font-weight:600}
.team > .wrap > p{position:absolute;top:129px;width:410px;font-size:10.5px;line-height:17.5px;color:var(--muted)}
.member{top:221px;width:243px;height:107px;padding:16px}
.avatar{width:35px;height:35px;background:var(--green);border:1px solid var(--line);font-family:"Space Mono",monospace;font-size:9px;display:flex;align-items:center;justify-content:center}
.member h4{font-size:10.5px;margin:15px 0 4px}
.member span{font-size:9px;color:var(--muted)}
.contact{position:absolute;top:363px;left:0;width:760px;height:330px;border:1.5px solid var(--line);display:flex;background:var(--white)}
.contact-info{width:380px;background:var(--green-dark);padding:26px;color:#e4eee0}
.contact-info h3{color:var(--white);font-size:20px;font-weight:600}
.contact-info p{font-size:10.5px;line-height:17.5px;margin:12px 0 20px}
.cline{display:flex;align-items:center;gap:9px;font-size:9.5px;color:var(--white);height:34px;border-bottom:1px solid rgba(255,255,255,.25);width:327px}
.cline:last-child{border:0}
.form{padding:25px;flex:1}
.form label{display:block;font-family:"Space Grotesk",sans-serif;font-weight:700;font-size:8px;letter-spacing:.8px;text-transform:uppercase;margin-bottom:7px}
.field{border:1px solid #9aa39b;height:27px;font-size:9px;color:#a8b0a9;padding:8px 10px;margin-bottom:14px}
.field.area{height:53px}
.form .btn{display:block;text-align:center;margin-top:12px;padding:8px}

/* footer */
.footer{height:294px;background:var(--green-dark);color:#d9e6d4;border:0}
.footer .brand{top:38px;color:var(--white)}
.footer .brand-mark{background:var(--green)}
.footer .about-text{position:absolute;top:82px;width:225px;font-size:10.5px;line-height:17.5px}
.footer .btn{position:absolute;top:162px;background:transparent;color:var(--white);border:1.5px solid var(--white);box-shadow:none}
.fcol{position:absolute;top:43px}
.fcol h5{font-family:"Space Mono",monospace;font-size:7.5px;letter-spacing:1.5px;font-weight:400;color:#a9c5a1;margin-bottom:9px}
.fcol div{display:flex;align-items:center;gap:8px;font-size:9.5px;height:21.5px;color:var(--white)}
.legal{position:absolute;top:222px;left:0;right:0;border-top:1px solid rgba(255,255,255,.3);padding-top:18px;display:flex;justify-content:space-between;font-size:8.5px}
.legal span:last-child{font-family:"Space Mono",monospace;letter-spacing:1.5px;font-size:7.5px}
</style>
</head>
<body>

<svg width="0" height="0" style="position:absolute">
  <defs>
    <linearGradient id="faceGrad" x1="0" y1="0" x2="1" y2="1">
      <stop offset="0" stop-color="#8fbf7f"/>
      <stop offset="1" stop-color="#2b5e34"/>
    </linearGradient>
    <g id="icosahedron" stroke="#2b5e34" stroke-width="1" stroke-linejoin="round">
      <polygon points="0,-50 43,-25 0,-22" fill="#8fbf7f"/>
      <polygon points="0,-50 -43,-25 0,-22" fill="#a9d09a"/>
      <polygon points="43,-25 19,11 0,-22" fill="#6fa862"/>
      <polygon points="-43,-25 -19,11 0,-22" fill="#86b978"/>
      <polygon points="43,-25 43,25 19,11" fill="#4f8a44"/>
      <polygon points="-43,-25 -43,25 -19,11" fill="#6fa862"/>
      <polygon points="43,25 0,50 19,11" fill="#3d6c32"/>
      <polygon points="-43,25 0,50 -19,11" fill="#4f8a44"/>
      <polygon points="0,50 19,11 -19,11" fill="#467c3b"/>
      <polygon points="0,-22 19,11 -19,11" fill="#5f9a53"/>
    </g>
    <g id="dodecahedron" stroke="#2b5e34" stroke-width="1" stroke-linejoin="round" fill="none">
      <polygon points="0,-48 28.2,-38.8 45.7,-14.8 45.7,14.8 28.2,38.8 0,48 -28.2,38.8 -45.7,14.8 -45.7,-14.8 -28.2,-38.8" fill="url(#faceGrad)" fill-opacity=".55"/>
      <polygon points="0,-22 20.9,-6.8 12.9,17.8 -12.9,17.8 -20.9,-6.8" fill="#3d6c32" fill-opacity=".7"/>
      <path d="M0,-22V-36M20.9,-6.8L34.2,-11.1M12.9,17.8L21.2,29.1M-12.9,17.8L-21.2,29.1M-20.9,-6.8L-34.2,-11.1"/>
      <path d="M-28.2,-38.8L0,-36L28.2,-38.8M28.2,-38.8L34.2,-11.1L45.7,14.8M45.7,14.8L21.2,29.1L0,48M0,48L-21.2,29.1L-45.7,14.8M-45.7,14.8L-34.2,-11.1L-28.2,-38.8"/>
    </g>
  </defs>
</svg>

<header class="nav" style="border-bottom:1.5px solid var(--line)">
  <div class="wrap">
    <div class="brand"><span class="brand-mark"></span>KEYSTONE</div>
    <nav class="menu"><span>HOME</span><span>PHILOSOPHY</span><span>BLOG</span><span>TEAM &amp; CONTACT</span></nav>
    <a class="btn" href="#">Request an Introduction</a>
  </div>
</header>

<section class="hero">
  <svg class="geo lattice-hero" style="left:985px;top:30px" width="215" height="330" viewBox="0 0 215 330" aria-hidden="true">
    <g stroke="#3d6c32" stroke-width="1" fill="none" opacity=".35">
      <path d="M20 40l45-26 45 26 45-26 45 26M20 40v52l45 26 45-26 45 26 45-26V40M65 14v0M65 66v52M110 40v52M155 66v52M65 66L20 40M65 66l45-26M155 66l-45-26M155 66l45-26"/>
      <path d="M20 144l45 26 45-26 45 26 45-26M20 92v52M200 92v52M65 118v52M155 118v52M110 92v52"/>
      <path d="M20 196l45 26 45-26 45 26 45-26M20 144v52M110 144v52M200 144v52M65 170v52M155 170v52" stroke-dasharray="4 4"/>
      <path d="M65 222v52M155 222v52M110 196v52" stroke-dasharray="2 5"/>
    </g>
    <g fill="#3d6c32" opacity=".55">
      <circle cx="20" cy="40" r="2.5"/><circle cx="110" cy="40" r="2.5"/><circle cx="200" cy="40" r="2.5"/>
      <circle cx="65" cy="66" r="2.5"/><circle cx="155" cy="66" r="2.5"/>
      <circle cx="20" cy="92" r="2.5"/><circle cx="110" cy="92" r="2.5"/><circle cx="200" cy="92" r="2.5"/>
      <circle cx="65" cy="118" r="2.5"/><circle cx="155" cy="118" r="2.5"/>
      <circle cx="20" cy="144" r="2.5"/><circle cx="110" cy="144" r="2.5"/><circle cx="200" cy="144" r="2.5"/>
      <circle cx="65" cy="170" r="2.5"/><circle cx="155" cy="170" r="2.5"/>
    </g>
  </svg>
  <div class="wrap">
    <div class="label">// 01 — Independent equity research &amp; investment</div>
    <h1>Disciplined research.<br><span>Patient capital.</span></h1>
    <p>Keystone Research &amp; Investment is an independent research-led investment firm. We study businesses the way founders do — deeply, patiently, and with a bias toward durable advantage over market noise — so capital compounds the way a stream widens as it runs its course.</p>
    <a class="btn" href="#">Request an Introduction</a>
    <a class="link" href="#">Our Philosophy →</a>
    <div class="stats">
      <div class="stat"><b>15+</b><i>Years of combined research experience</i></div>
      <div class="stat"><b>30–50</b><i>Concentrated portfolio positions</i></div>
      <div class="stat"><b>1</b><i>Investment philosophy, applied consistently</i></div>
    </div>
    <svg class="geo" style="left:420px;top:300px" width="80" height="80" viewBox="-52 -52 104 104" aria-hidden="true"><use href="#icosahedron" opacity=".8"/></svg>
  </div>
</section>

<section class="about">
  <div class="wrap">
    <div class="label">// 02 — Who we are</div>
    <h2>Research first. Everything else follows.</h2>
    <p>We built Keystone Research &amp; Investment on a simple premise: markets reward the investors who understand a business better than the crowd does, and who have the patience to wait for that understanding to be recognized. We are not a mass-market product — we work face-to-face with a select group of professional investors who share our horizon and our discipline.</p>
    <a class="link" href="#">Speak with our team →</a>

    <div class="card feature" style="left:263px;top:62px"><span class="num">01</span>
      <div class="icon"><svg width="14" height="12" viewBox="0 0 14 12"><path d="M1 11h12M2 9l4-3 3 2 4-6" fill="none" stroke="#4aa63f" stroke-width="1"/></svg></div>
      <h4>Primary Research</h4><p>Original, bottom-up analysis of company fundamentals, industry structure, and competitive positioning.</p></div>
    <div class="card feature" style="left:519px;top:62px"><span class="num">02</span>
      <div class="icon"><svg width="12" height="12" viewBox="0 0 12 12"><circle cx="6" cy="6" r="5" fill="none" stroke="#cfe0c8"/><circle cx="6" cy="6" r="2" fill="#4aa63f"/></svg></div>
      <h4>Concentrated Portfolios</h4><p>A limited number of high-conviction positions, sized to reflect our confidence, not an index weighting.</p></div>
    <div class="card feature" style="left:263px;top:216px"><span class="num">03</span>
      <div class="icon"><svg width="14" height="12" viewBox="0 0 14 12"><circle cx="4" cy="6" r="3" fill="none" stroke="#4aa63f"/><path d="M8 6h5M11 4l2 2-2 2" fill="none" stroke="#4aa63f"/></svg></div>
      <h4>Direct Access</h4><p>A firm structured for face-to-face relationships with our investors, not broad distribution.</p></div>
    <div class="card feature" style="left:519px;top:216px"><span class="num">04</span>
      <div class="icon"><svg width="12" height="12" viewBox="0 0 12 12"><path d="M6 2L10 10H2Z" fill="none" stroke="#4aa63f"/></svg></div>
      <h4>Alignment</h4><p>We invest alongside our clients and measure ourselves by the same time horizon we ask of them.</p></div>
  </div>
</section>

<section class="philosophy">
  <div class="wrap">
    <div class="label">// 03 — Investment philosophy</div>
    <h2>Three principles, applied without exception</h2>
    <p>Our approach is deliberately narrow. We would rather do a few things exceptionally well than many things adequately — the same discipline we look for in the businesses we back.</p>
    <svg class="geo" style="left:520px;top:50px" width="240" height="170" viewBox="0 0 240 170" aria-hidden="true">
      <g stroke="#3d6c32" stroke-width="1" opacity=".35" fill="none" stroke-dasharray="3 4">
        <path d="M60 85L170 60M60 85L180 130M170 60L180 130"/>
      </g>
      <g transform="translate(62 86) scale(1.05)"><use href="#dodecahedron"/></g>
      <g transform="translate(175 58) scale(.72)"><use href="#icosahedron" opacity=".9"/></g>
      <g transform="translate(190 135) scale(.38)"><use href="#icosahedron" opacity=".55"/></g>
    </svg>
    <div class="card pcard" style="left:0"><span class="tag">01</span><h4>Own Businesses, Not Tickers</h4><p>We evaluate companies as private owners would — by their economics, governance, and ability to compound capital over years, not by short-term price movement.</p></div>
    <div class="card pcard" style="left:258px"><span class="tag">02</span><h4>Insist on a Margin of Safety</h4><p>Every position is sized against a disciplined estimate of intrinsic value, leaving room for the analysis to be wrong without capital being permanently impaired.</p></div>
    <div class="card pcard" style="left:517px"><span class="tag">03</span><h4>Let the Stream Widen</h4><p>Compounding rewards patience. We resist the urge to trade around conviction and let well-chosen positions broaden in value over full market cycles.</p></div>
    <a class="btn ghost" href="#">Read our full philosophy</a>
  </div>
</section>

<section class="insights">
  <div class="wrap">
    <div class="label">// 04 — From the research desk</div>
    <h2>Recent Insights</h2>
    <a class="link all" href="#">View all posts →</a>
    <div class="card post" style="left:0">
      <svg width="22" height="14" viewBox="0 0 22 14"><path d="M2 13v-3M7 13v-5M12 13v-2M18 13V1" stroke="#9aa39b"/></svg>
      <div class="meta">Research notes · 7 min read</div><h4>What Separates a Compounder from a Cyclical Winner</h4><p>A framework for distinguishing durable competitive advantage from a temporary cyclical tailwind — and why the distinction matters more than the multiple you pay.</p><a class="link" href="#">Read the note →</a></div>
    <div class="card post" style="left:258px">
      <svg width="18" height="18" viewBox="0 0 18 18"><circle cx="9" cy="9" r="7.5" fill="none" stroke="#cfe0c8"/><circle cx="9" cy="9" r="3" fill="#4aa63f"/></svg>
      <div class="meta" style="margin-top:10px">Portfolio strategy · 5 min read</div><h4>The Case for a Concentrated Portfolio</h4><p>Why owning fewer businesses, understood deeply, tends to outperform owning many, understood superficially — and how we manage the risk that comes with it.</p><a class="link" href="#">Read the note →</a></div>
    <div class="card post" style="left:517px">
      <svg width="24" height="14" viewBox="0 0 24 14"><path d="M1 12l7-5 5 3 9-8" fill="none" stroke="#5d665f"/></svg>
      <div class="meta">Market commentary · 6 min read</div><h4>Reading a Cycle Without Trading It</h4><p>Our view on why acknowledging where we are in a cycle need not translate into tactical trading — and how we stay anchored to fundamentals regardless.</p><a class="link" href="#">Read the note →</a></div>
  </div>
</section>

<section class="team">
  <div class="wrap">
    <div class="label">// 05 — Team &amp; contact</div>
    <h2>A small team, deliberately</h2>
    <p>Keystone Research &amp; Investment is led by a compact group of analysts and portfolio managers who each carry deep sector expertise. We meet our investors directly — no intermediaries, no mass distribution — because the relationships that matter to us are built in conversation, not in a pitch deck.</p>
    <svg class="geo" style="left:470px;top:55px" width="290" height="150" viewBox="0 0 290 150" aria-hidden="true">
      <g stroke="#3d6c32" stroke-width="1" fill="none">
        <g opacity=".55">
          <path d="M150 30l40-22 40 22-40 22zM150 30v44l40 22V52M230 30v44l-40 22"/>
          <path d="M190 52l40-22 40 22-40 22zM270 52v44l-40 22V74"/>
          <path d="M110 52l40-22 40 22-40 22zM110 52v44l40 22V74"/>
        </g>
        <path d="M150 74v44M190 96v44M110 96l40 22 40-22M190 140l40-22" opacity=".35" stroke-dasharray="4 4"/>
      </g>
      <g>
        <polygon points="150,30 190,8 230,30 190,52" fill="#8fbf7f" opacity=".45"/>
        <polygon points="150,30 190,52 190,96 150,74" fill="#3d6c32" opacity=".35"/>
        <polygon points="190,52 230,30 230,74 190,96" fill="#2b5e34" opacity=".5"/>
        <polygon points="230,74 270,52 270,96 230,118" fill="#3d6c32" opacity=".25"/>
      </g>
      <g fill="#3d6c32" opacity=".6">
        <circle cx="150" cy="30" r="2.5"/><circle cx="190" cy="8" r="2.5"/><circle cx="230" cy="30" r="2.5"/><circle cx="190" cy="52" r="2.5"/><circle cx="270" cy="52" r="2.5"/><circle cx="110" cy="52" r="2.5"/><circle cx="190" cy="96" r="2.5"/><circle cx="230" cy="74" r="2.5"/>
      </g>
      <g transform="translate(45 100) scale(.55)"><use href="#dodecahedron" opacity=".7"/></g>
    </svg>
    <div class="card member" style="left:0"><div class="avatar">MP</div><h4>Managing Partner</h4><span>Investment Strategy &amp; Portfolio Management</span></div>
    <div class="card member" style="left:258px"><div class="avatar">HR</div><h4>Head of Research</h4><span>Fundamental Analysis &amp; Diligence</span></div>
    <div class="card member" style="left:517px"><div class="avatar">IR</div><h4>Investor Relations</h4><span>Client Partnerships &amp; Reporting</span></div>

    <div class="contact">
      <div class="contact-info">
        <h3>Request an Introduction</h3>
        <p>Our work is by introduction and direct conversation. If you are a professional investor and would like to learn more about our approach, reach out — we respond personally to every inquiry.</p>
        <div class="cline"><svg width="11" height="9" viewBox="0 0 11 9"><rect x=".5" y=".5" width="10" height="8" fill="none" stroke="#4aa63f"/><path d="M.5 .5l5 4 5-4" fill="none" stroke="#4aa63f"/></svg>invest@keystoneresearch.example</div>
        <div class="cline"><svg width="11" height="11" viewBox="0 0 11 11"><path d="M2 1l2 2-1 2 3 3 2-1 2 2-2 2C4 10 1 7 0 3Z" fill="none" stroke="#4aa63f"/></svg>+1 (212) 555-0187</div>
        <div class="cline"><svg width="10" height="12" viewBox="0 0 10 12"><path d="M5 11S1 7 1 4.5a4 4 0 018 0C9 7 5 11 5 11Z" fill="none" stroke="#4aa63f"/><circle cx="5" cy="4.5" r="1.3" fill="none" stroke="#4aa63f"/></svg>New York, NY — by appointment only</div>
      </div>
      <div class="form">
        <label>Full name</label><div class="field">Jane Doe</div>
        <label>Email address</label><div class="field">jane@firm.com</div>
        <label>Firm / Institution</label><div class="field">Firm name</div>
        <label>Message</label><div class="field area">Tell us a little about your mandate.</div>
        <a class="btn" href="#">Send Message</a>
      </div>
    </div>
  </div>
</section>

<footer class="footer">
  <div class="wrap">
    <div class="brand"><span class="brand-mark"></span>KEYSTONE</div>
    <p class="about-text">Keystone Research &amp; Investment is an independent equity research and investment management firm serving select professional investors.</p>
    <a class="btn" href="#">Request an Introduction</a>
    <div class="fcol" style="left:327px"><h5>NAVIGATE</h5>
      <div><svg width="9" height="9" viewBox="0 0 9 9"><path d="M1 4.5L4.5 1 8 4.5V8H1Z" fill="none" stroke="#a9c5a1"/></svg>Home</div>
      <div><svg width="9" height="9" viewBox="0 0 9 9"><rect x=".5" y="1.5" width="8" height="6" fill="none" stroke="#a9c5a1"/></svg>Investment Philosophy</div>
      <div><svg width="9" height="9" viewBox="0 0 9 9"><rect x="1.5" y=".5" width="6" height="8" fill="none" stroke="#a9c5a1"/></svg>Blog</div>
      <div><svg width="9" height="9" viewBox="0 0 9 9"><circle cx="3" cy="3" r="2" fill="none" stroke="#a9c5a1"/><path d="M0 8.5a3 3 0 016 0" fill="none" stroke="#a9c5a1"/></svg>Team &amp; Contact</div>
    </div>
    <div class="fcol" style="left:523px"><h5>CONTACT</h5>
      <div><svg width="9" height="8" viewBox="0 0 9 8"><rect x=".5" y=".5" width="8" height="7" fill="none" stroke="#a9c5a1"/></svg>invest@keystoneresearch.example</div>
      <div><svg width="9" height="9" viewBox="0 0 11 11"><path d="M2 1l2 2-1 2 3 3 2-1 2 2-2 2C4 10 1 7 0 3Z" fill="none" stroke="#a9c5a1"/></svg>+1 (212) 555-0187</div>
      <div><svg width="8" height="10" viewBox="0 0 10 12"><path d="M5 11S1 7 1 4.5a4 4 0 018 0C9 7 5 11 5 11Z" fill="none" stroke="#a9c5a1"/></svg>New York, NY — by appointment only</div>
    </div>
    <div class="legal"><span>© 2026 Keystone Research &amp; Investment. All rights reserved. For professional investors only. Not a solicitation.</span><span>BACK TO TOP ↑</span></div>
  </div>
</footer>

</body>
</html>
```